Business Card Design

Voltline Contracting
need a buisness card relating to that buisness

Reason: Just need to discuss with partner

Industry/Entity Type

Business

Contact Information for Business Card

Dale Fenwick Electrical
0431 756 918
dalefenwick7@mailnest.example
REC 58714

```html
<!DOCTYPE html>
<html lang="en">
<head>
<meta charset="utf-8">
<title>Dale Fenwick Electrical – Business Card</title>
<link rel="stylesheet" href="https://fonts.googleapis.com/css2?family=Oswald:wght@500;600&family=Open+Sans:wght@400&display=swap">
<style>
  :root {
    --page-bg: #e4e4e4;
    --card-white: #ffffff;
    --card-tint: #ededed;
    --ink-dark: #1e1e1e;
    --ink-grey: #5a5a5a;
    --accent-orange: #f07a1a;
  }
  html, body {
    margin: 0;
    width: 1200px;
    height: 1000px;
    overflow: hidden;
    background: var(--page-bg);
  }
  .business-card {
    position: absolute;
    left: 150px;
    top: 242px;
    width: 900px;
    height: 516px;
    background: var(--card-white);
    box-shadow: 0 10px 30px rgba(0,0,0,0.18);
    overflow: hidden;
  }
  .card-texture {
    position: absolute;
    inset: 0;
    background: radial-gradient(ellipse at 45% 55%, var(--card-tint) 0%, var(--card-white) 70%);
  }
  .brand {
    position: absolute;
    top: 78px;
    left: 0;
    right: 0;
    display: flex;
    justify-content: center;
    align-items: center;
    gap: 16px;
  }
  .brand-dot {
    width: 46px;
    height: 46px;
    border-radius: 50%;
    background: var(--accent-orange);
  }
  .brand-name {
    font-family: "Oswald", sans-serif;
    font-weight: 500;
    font-size: 26px;
    letter-spacing: 1px;
    text-transform: uppercase;
    color: var(--ink-grey);
  }
  .holder {
    position: absolute;
    top: 186px;
    left: 0;
    right: 0;
    text-align: center;
  }
  .holder-name {
    font-family: "Oswald", sans-serif;
    font-weight: 600;
    font-size: 34px;
    letter-spacing: 0.5px;
    text-transform: uppercase;
    color: var(--ink-dark);
  }
  .holder-trade {
    font-family: "Open Sans", sans-serif;
    font-size: 17px;
    color: var(--ink-dark);
    margin-left: 8px;
  }
  .contact {
    position: absolute;
    top: 300px;
    left: 0;
    right: 0;
    display: flex;
    flex-direction: column;
    align-items: center;
    gap: 6px;
    font-family: "Open Sans", sans-serif;
    font-size: 19px;
    color: var(--ink-dark);
  }
  .contact-line {
    display: flex;
    align-items: center;
    gap: 10px;
  }
  .contact-icon {
    width: 22px;
    height: 18px;
    fill: none;
    stroke: var(--accent-orange);
    stroke-width: 1.8;
  }
  .contact-icon.phone {
    fill: var(--accent-orange);
    stroke: none;
    width: 16px;
  }
</style>
</head>
<body>
  <section class="business-card">
    <div class="card-texture" role="img" aria-label="Faint grey circuit board pattern across the card"></div>

    <div class="brand">
      <span class="brand-dot"></span>
      <span class="brand-name">Voltline Contracting</span>
    </div>

    <div class="holder">
      <span class="holder-name">Dale Fenwick</span><span class="holder-trade">Electrical</span>
    </div>

    <div class="contact">
      <div class="contact-line">
        <svg class="contact-icon phone" viewBox="0 0 16 18" aria-hidden="true">
          <path d="M4 1 L7 4 L5 7 C6 10 8 12 10 13 L12.5 11 L15 14 L13 17 C7 16 2 10 1 4 Z"/>
        </svg>
        <span>0431 756 918</span>
      </div>
      <div class="contact-line">
        <svg class="contact-icon" viewBox="0 0 22 18" aria-hidden="true">
          <rect x="1.5" y="2" width="19" height="14"/>
          <path d="M1.5 2 L11 10 L20.5 2"/>
        </svg>
        <span>dalefenwick7@mailnest.example</span>
      </div>
      <div class="contact-line">
        <span>REC 58714</span>
      </div>
    </div>
  </section>
</body>
</html>
```